Dane Calloway Photography

Would like the Business card to have a cool logo. I’m targeting wedding/ engagement: portrait photography. My phone number on it. And my business email address.

Target Market(s)

Wedding/portrait/engagement photography.

```html
<!DOCTYPE html>
<html lang="en">
<head>
<meta charset="utf-8">
<title>Dane Calloway Photography – Business Card</title>
<link rel="stylesheet" href="https://fonts.googleapis.com/css2?family=Oswald:wght@300&family=Open+Sans:wght@400;700&display=swap">
<style>
  :root {
    --backdrop: #3a2a1f;
    --card: #4a4a3b;
    --cream: #fbf3d2;
    --white: #ffffff;
    --teal: #1fbfa8;
  }
  * { margin: 0; padding: 0; box-sizing: border-box; }
  html, body {
    width: 1200px;
    height: 1189px;
    overflow: hidden;
    background: var(--backdrop);
  }
  .canvas {
    position: relative;
    width: 1200px;
    height: 1189px;
  }
  .card {
    position: absolute;
    left: 100px;
    top: 324px;
    width: 1000px;
    height: 540px;
    border-radius: 44px;
    background: var(--card);
    box-shadow: 0 18px 40px rgba(0,0,0,0.45);
  }
  .brand {
    position: absolute;
    left: 70px;
    top: 150px;
    width: 360px;
    text-align: center;
    font-family: "Oswald", sans-serif;
    font-weight: 300;
    color: var(--white);
  }
  .brand-mark {
    display: block;
    width: 40px;
    height: 40px;
    margin: 0 auto 26px;
    background: var(--teal);
  }
  .brand-name {
    font-size: 56px;
    line-height: 1.1;
    letter-spacing: 1px;
  }
  .brand-tagline {
    margin-top: 10px;
    font-size: 40px;
    line-height: 1.1;
  }
  .contact {
    position: absolute;
    left: 520px;
    top: 150px;
    color: var(--cream);
  }
  .contact-name {
    font-family: "Oswald", sans-serif;
    font-weight: 300;
    font-size: 50px;
    line-height: 1;
    text-transform: uppercase;
  }
  .contact-email {
    font-family: "Open Sans", sans-serif;
    font-size: 21px;
    margin-top: 6px;
  }
  .contact-address {
    font-family: "Open Sans", sans-serif;
    font-size: 21px;
    line-height: 1.4;
    margin-top: 26px;
    padding-left: 12px;
    text-transform: uppercase;
  }
  .contact-phone {
    font-family: "Open Sans", sans-serif;
    font-weight: 700;
    font-size: 34px;
    margin-top: 18px;
    padding-left: 14px;
    letter-spacing: 1px;
  }
</style>
</head>
<body>
<main class="canvas">
  <section class="card">
    <div class="brand">
      <span class="brand-mark"></span>
      <p class="brand-name">Dane Calloway</p>
      <p class="brand-tagline">Photography</p>
    </div>
    <div class="contact">
      <h1 class="contact-name">Dane Calloway</h1>
      <p class="contact-email">danecalloway@studiomail.com</p>
      <p class="contact-address">Linden Avenue 31207<br>Harbor Vale 06712</p>
      <p class="contact-phone">555 0142 7731</p>
    </div>
  </section>
</main>
</body>
</html>
```